PRVD Traditional Business Card Project

Please see attached....just a simple business card... on attachment- please use the exact font, style, etc as the attached "Pat Everard Wynne" card... however, replace with the "Owen Reginald Talbot" text and address below the card.

```html
<!DOCTYPE html>
<html lang="en">
<head>
<meta charset="utf-8">
<title>PRVD Business Card</title>
<link rel="stylesheet" href="https://fonts.googleapis.com/css2?family=Playfair+Display+SC:wght@700&family=Montserrat:wght@500&display=swap">
<style>
  :root {
    --backdrop: #8e9091;
    --card: #d9dddc;
    --ink: #1c1d1d;
    --ink-soft: #2e3030;
    --bracket: #ffffff;
  }
  html, body {
    margin: 0;
    width: 1200px;
    height: 834px;
    overflow: hidden;
    background: var(--backdrop);
  }
  .card {
    position: absolute;
    left: 100px;
    top: 131px;
    width: 1000px;
    height: 572px;
    background: var(--card);
    color: var(--ink);
    box-shadow: 0 6px 20px rgba(0,0,0,0.25);
  }
  .corner {
    position: absolute;
    width: 44px;
    height: 44px;
  }
  .corner--top-left { left: 14px; top: 14px; }
  .corner--bottom-right { right: 14px; bottom: 14px; transform: rotate(180deg); }
  .firm {
    position: absolute;
    left: 62px;
    top: 52px;
  }
  .firm__name {
    font-family: "Playfair Display SC", Georgia, serif;
    font-weight: 700;
    font-size: 34px;
    letter-spacing: 1px;
    line-height: 1;
  }
  .firm__tagline {
    font-family: "Montserrat", Arial, sans-serif;
    font-weight: 500;
    font-size: 13px;
    letter-spacing: 3px;
    margin-top: 8px;
    color: var(--ink-soft);
  }
  .attorney {
    position: absolute;
    left: 200px;
    top: 150px;
    text-align: center;
  }
  .attorney__name {
    font-family: "Playfair Display SC", Georgia, serif;
    font-weight: 700;
    font-size: 58px;
    letter-spacing: 2px;
    line-height: 1;
    text-shadow: 0 1px 0 rgba(255,255,255,0.4);
  }
  .attorney__title {
    font-family: "Montserrat", Arial, sans-serif;
    font-weight: 500;
    font-size: 16px;
    letter-spacing: 7px;
    margin-top: 12px;
    color: var(--ink-soft);
  }
  .address, .contact {
    position: absolute;
    font-family: "Montserrat", Arial, sans-serif;
    font-weight: 500;
    font-size: 19px;
    letter-spacing: 1.5px;
    line-height: 1.35;
    color: var(--ink-soft);
  }
  .address { left: 62px; top: 286px; }
  .contact { right: 70px; bottom: 62px; }
  .address p, .contact p { margin: 0; }
</style>
</head>
<body>
  <section class="card" aria-label="PRVD business card">
    <svg class="corner corner--top-left" viewBox="0 0 44 44" aria-hidden="true">
      <path d="M3 44 V3 H44" fill="none" stroke="var(--bracket)" stroke-width="5"/>
    </svg>
    <svg class="corner corner--bottom-right" viewBox="0 0 44 44" aria-hidden="true">
      <path d="M3 44 V3 H44" fill="none" stroke="var(--bracket)" stroke-width="5"/>
    </svg>

    <header class="firm">
      <div class="firm__name">Pacific Ridge</div>
      <div class="firm__tagline">LAWYERS GROUP, PLC</div>
    </header>

    <div class="attorney">
      <div class="attorney__name">Owen Reginald Talbot</div>
      <div class="attorney__title">ATTORNEY AT LAW</div>
    </div>

    <address class="address">
      <p>2740 CEDAR AVENUE, SUITE B</p>
      <p>ALDER HILLS, CA 90412</p>
      <p>www.lawprvd.com</p>
    </address>

    <div class="contact">
      <p>TEL (555) 214-7300</p>
      <p>FAX (555) 214-7301</p>
      <p>otalbot@lawprvd.com</p>
    </div>
  </section>
</body>
</html>
```